Business Card for Marriage Commissioner

I am a marriage commissioner in the province of Alberta, meaning that I perform civil unions here. I have been trying to think of a unique design for my business card, something a bit different. A lot of "unique" designs seem to incorporate unique cuts or "some assembly required" or printed on plastic or meat. I would like my design to be a full colour card that is a typical business card size.

The information on the card should have:
Lou Varnik
my occupation: Marriage Commissioner
my website: www.louvarnik.ca
my e-mail: lou@louvarnik.ca
my phone: 780-418-2964

I originally submitted a design to the printer that had a screen capture of a findly search window, with my name and occupation in the text box. And underneath that, my phone number. Nothing else. They indicated they could not print this because it was a copyright violation.

One option on the design is I am a retired chemist-so a chemistry themed card would also be of interest, as long as it isn't a "Rusted Tide" theme, as I have that on my other business cards already...

I would prefer a single sided card, but I am open to a double sided card if it is clever!

I would also prefer not to have pictures of male and female couples as in my position I will also marry same sex couples. Same thing for male/female symbols. Someone has submitted two graduated cylinders in love, which is very clever, and gets around this male/female type.

Thanks for your help and interest.

Target Market(s)

Young couples.

Industry/Entity Type

Plastic

Requirements
Nice to have
• chemistry ideas!
Should not have
• Male/female pictures, male/female symbols.
No QR codes.
No transparent designs, will go on paper stock.

```html
<!DOCTYPE html>
<html lang="en">
<head>
<meta charset="utf-8">
<title>Lou Varnik – Marriage Commissioner Business Card</title>
<link rel="stylesheet" href="https://fonts.googleapis.com/css2?family=Source+Sans+3:wght@400;700&display=swap">
<style>
  :root {
    --backdrop: #e9e6e2;
    --card-green: #439a45;
    --accent-red: #e33c26;
    --ink-dark: #231f20;
    --text-light: #ffffff;
  }
  html, body {
    margin: 0;
    padding: 0;
    width: 1200px;
    height: 1000px;
    overflow: hidden;
    background: var(--backdrop);
    font-family: "Source Sans 3", "Myriad Pro", Arial, sans-serif;
  }
  .business-card {
    position: absolute;
    left: 100px;
    top: 214px;
    width: 1000px;
    height: 572px;
    background: var(--card-green);
    overflow: hidden;
    box-shadow: 0 10px 30px rgba(0,0,0,0.18);
  }
  .card-art {
    position: absolute;
    inset: 0;
    width: 1000px;
    height: 572px;
  }
  .red-field { fill: var(--accent-red); }
  .emblem-area { fill: var(--ink-dark); }
  .identity {
    position: absolute;
    left: 585px;
    top: 118px;
    color: var(--text-light);
  }
  .identity-name {
    margin: 0;
    font-size: 34px;
    font-weight: 700;
    line-height: 1.1;
  }
  .identity-role {
    margin: 4px 0 0 14px;
    font-size: 25px;
    font-weight: 400;
  }
  .contact-list {
    position: absolute;
    left: 600px;
    top: 318px;
    margin: 0;
    padding: 0;
    list-style: none;
    color: var(--text-light);
    font-size: 28px;
  }
  .contact-item {
    display: flex;
    align-items: center;
    gap: 14px;
    height: 44px;
  }
  .contact-item:nth-child(2) { margin-left: 14px; }
  .contact-item:nth-child(3) { margin-left: 28px; }
  .contact-badge {
    flex: none;
    width: 26px;
    height: 26px;
    border-radius: 50%;
    background: var(--accent-red);
    color: var(--card-green);
    font-size: 15px;
    font-weight: 700;
    line-height: 1;
    display: flex;
    align-items: center;
    justify-content: center;
  }
</style>
</head>
<body>
  <article class="business-card">
    <svg class="card-art" viewBox="0 0 1000 572">
      <path class="red-field" d="M0 0 H300 A255 255 0 0 1 300 572 H0 Z"/>
      <circle class="emblem-area" cx="285" cy="360" r="155" role="img" aria-label="Card emblem"/>
    </svg>
    <header class="identity">
      <h1 class="identity-name">Lou Varnik</h1>
      <p class="identity-role">Marriage Commissioner</p>
    </header>
    <ul class="contact-list">
      <li class="contact-item"><span class="contact-badge">M</span><span class="contact-text">780-418-2964</span></li>
      <li class="contact-item"><span class="contact-badge">E</span><span class="contact-text">lou@louvarnik.ca</span></li>
      <li class="contact-item"><span class="contact-badge">W</span><span class="contact-text">www.louvarnik.ca</span></li>
    </ul>
  </article>
</body>
</html>
```